Copper Lantern Podcast Business Card Design

Needing a business card with the logo design provided for Copper Lantern Podcast. I am looking for a modern style that fits the current logo.

Info:
Name: Bao Khanh
Title: Creator/Host
Email: bao@copperlanternpod.com
Phone: (405) 637-2918
www.copperlanternpod.com
Twitter: @coplanternpod
Instagram: @copperlanternpodcast
Facebook: Copper Lantern Podcast

Industry/Entity Type

Business

Font styles to use
Sans Serif

Colors
000000
ffffff

Requirements
Must have
• modern, clean design
Nice to have
• social media contact info

```html
<!DOCTYPE html>
<html lang="en">
<head>
<meta charset="UTF-8">
<title>Copper Lantern Podcast – Business Cards</title>
<link href="https://fonts.googleapis.com/css2?family=Montserrat:wght@600;700;800&family=Roboto:wght@400;500&display=swap" rel="stylesheet">
<style>
  :root {
    --ink: #000000;
    --paper: #ffffff;
    --stage: #1b1b1b;
    --muted: #d9d9d9;
  }
  html, body {
    margin: 0;
    padding: 0;
    width: 1200px;
    height: 900px;
    overflow: hidden;
    background: var(--stage);
  }
  .canvas {
    position: relative;
    width: 1200px;
    height: 900px;
  }
  .card {
    position: absolute;
    left: 240px;
    width: 720px;
    height: 410px;
    overflow: hidden;
    box-shadow: 0 10px 30px rgba(0,0,0,.6);
  }
  .card--back { top: 30px; background: var(--ink); }
  .card--front { top: 460px; background: var(--paper); }
  .card svg.shapes { position: absolute; inset: 0; }

  .wordmark {
    position: absolute;
    display: flex;
    align-items: center;
    gap: 12px;
    font-family: 'Montserrat', sans-serif;
    font-weight: 800;
    letter-spacing: .5px;
    white-space: nowrap;
  }
  .wordmark__square {
    width: 22px;
    height: 22px;
  }

  /* back */
  .card--back .wordmark {
    left: 0; right: 0; top: 212px;
    justify-content: center;
    color: var(--paper);
    font-size: 30px;
  }
  .card--back .wordmark__square { background: var(--paper); }

  /* front */
  .card--front .wordmark {
    left: 0; right: 0; top: 110px;
    justify-content: center;
    color: var(--ink);
    font-size: 30px;
  }
  .card--front .wordmark__square { background: var(--ink); }

  .person {
    position: absolute;
    left: 372px;
    top: 196px;
    font-family: 'Montserrat', sans-serif;
    color: var(--ink);
  }
  .person__name { font-weight: 800; font-size: 21px; letter-spacing: .5px; }
  .person__title { font-weight: 600; font-size: 12px; letter-spacing: 1px; margin-top: 2px; }

  .contacts, .socials {
    position: absolute;
    list-style: none;
    margin: 0;
    padding: 0;
    font-family: 'Roboto', sans-serif;
    font-size: 13.5px;
    color: var(--muted);
  }
  .contacts { left: 26px; top: 296px; }
  .socials { right: 26px; top: 296px; text-align: right; }
  .contacts li, .socials li {
    display: flex;
    align-items: center;
    gap: 10px;
    height: 28px;
  }
  .socials li { justify-content: flex-end; }
  .icon {
    width: 18px;
    height: 18px;
    border-radius: 50%;
    background: var(--paper);
    display: inline-flex;
    align-items: center;
    justify-content: center;
    flex: none;
  }
  .icon svg { width: 11px; height: 11px; }
</style>
</head>
<body>
<main class="canvas">

  <!-- Back of card -->
  <section class="card card--back" aria-label="Card back">
    <svg class="shapes" width="720" height="410" viewBox="0 0 720 410" aria-hidden="true">
      <rect x="0" y="100" width="300" height="90" fill="var(--paper)"/>
      <rect x="420" y="100" width="300" height="90" fill="var(--paper)"/>
    </svg>
    <div class="wordmark">
      <span class="wordmark__square"></span>
      <span>COPPER LANTERN PODCAST</span>
    </div>
  </section>

  <!-- Front of card -->
  <section class="card card--front" aria-label="Card front">
    <svg class="shapes" width="720" height="410" viewBox="0 0 720 410" aria-hidden="true">
      <rect x="0" y="258" width="720" height="3" fill="var(--ink)"/>
      <rect x="0" y="270" width="720" height="140" fill="var(--ink)"/>
      <line x1="300" y1="410" x2="420" y2="270" stroke="var(--paper)" stroke-width="3"/>
    </svg>

    <div class="wordmark">
      <span class="wordmark__square"></span>
      <span>COPPER LANTERN PODCAST</span>
    </div>

    <div class="person">
      <div class="person__name">BAO KHANH</div>
      <div class="person__title">CREATOR/HOST</div>
    </div>

    <ul class="contacts">
      <li>
        <span class="icon">
          <svg viewBox="0 0 24 24"><path d="M6.6 10.8a15 15 0 0 0 6.6 6.6l2.2-2.2c.3-.3.7-.4 1-.2 1.1.4 2.3.6 3.6.6.6 0 1 .4 1 1V20c0 .6-.4 1-1 1C10.6 21 3 13.4 3 4c0-.6.4-1 1-1h3.5c.6 0 1 .4 1 1 0 1.3.2 2.5.6 3.6.1.3 0 .7-.2 1z" fill="var(--ink)"/></svg>
        </span>
        (405) 637-2918
      </li>
      <li>
        <span class="icon">
          <svg viewBox="0 0 24 24"><rect x="3" y="6" width="18" height="12" fill="none" stroke="var(--ink)" stroke-width="2.4"/><path d="M3 6l9 7 9-7" fill="none" stroke="var(--ink)" stroke-width="2.4"/></svg>
        </span>
        bao@copperlanternpod.com
      </li>
      <li>
        <span class="icon">
          <svg viewBox="0 0 24 24"><circle cx="12" cy="12" r="9" fill="none" stroke="var(--ink)" stroke-width="2.2"/><path d="M3 12h18M12 3c3 3 3 15 0 18M12 3c-3 3-3 15 0 18" fill="none" stroke="var(--ink)" stroke-width="1.8"/></svg>
        </span>
        www.copperlanternpod.com
      </li>
    </ul>

    <ul class="socials">
      <li>@coplanternpod <span class="icon"></span></li>
      <li>@copperlanternpodcast <span class="icon"></span></li>
      <li>Copper Lantern Podcast <span class="icon"></span></li>
    </ul>
  </section>

</main>
</body>
</html>
```